Boutique Health and Fitness Personal Training Studio

I would like to have a brochure designed which provides a detailed description of the services offered in my business.
I have personal training studio, We look after people from early 20's to 90's, healthy to very unhealthy.
We conduct:
A consultation
An assessment
A personalised program
Personalised training sessions
I would like to base the design around the colours of my logo (attached) and use some of (or all of) the images and information I have also attached.
I would be happy with your own images included also.

Target Market(s)

20 to 90 year olds

Industry/Entity Type

Business

Font styles to use
Serif
Sans Serif

Colors
9bcb3c
add136
cadf82
eaf2ce

Requirements
Must have
• Colour and images of fitness.
• 8.5x14 legal
• Tri fold
• 2 folds with 3 faces back n front
Nice to have
• The feeling of wellbeing
Should not have
• This is not a gym.
• It should have the feel of a private relaxed environment

```html
<!DOCTYPE html>
<html lang="en">
<head>
<meta charset="utf-8">
<title>Evergreen Wellness Studio – Tri-fold Brochure</title>
<link href="https://fonts.googleapis.com/css2?family=Montserrat:wght@400;600;700;800&family=Open+Sans:wght@400;600&display=swap" rel="stylesheet">
<style>
  :root{
    --green:#9bcb3c;
    --green-deep:#6fa52a;
    --green-dark:#3f6b1c;
    --lime:#add136;
    --green-soft:#cadf82;
    --green-pale:#eaf2ce;
    --ink:#3b3f38;
    --muted:#6b7066;
    --paper:#ffffff;
    --stage:#dcdedb;
  }
  *{box-sizing:border-box;margin:0;padding:0}
  html,body{width:874px;height:1200px;overflow:hidden}
  body{background:var(--stage);font-family:"Open Sans",Arial,sans-serif;color:var(--ink);position:relative}
  .sheet{position:absolute;left:30px;width:815px;height:555px;background:var(--paper);overflow:hidden;box-shadow:0 4px 14px rgba(0,0,0,.18)}
  .sheet--outside{top:22px}
  .sheet--inside{top:612px}
  .panel{position:absolute;top:0;width:271.67px;height:555px;overflow:hidden}
  .panel--1{left:0}.panel--2{left:271.67px}.panel--3{left:543.33px}
  .fold{position:absolute;top:0;width:1px;height:555px;background:rgba(0,0,0,.06);z-index:5}
  .photo{position:absolute;background:linear-gradient(135deg,var(--green-soft),var(--green-deep))}
  .photo--warm{background:linear-gradient(135deg,#e9e2d6,#b9a995)}
  .photo--food{background:linear-gradient(135deg,#d94b2b,#f1b233 50%,#6fa52a)}
  .photo--dark{background:linear-gradient(160deg,#4d6b2e,#1f3110)}
  .heading{font-family:"Montserrat",Arial,sans-serif;font-weight:800;color:var(--green-deep);text-transform:uppercase;font-size:13px;line-height:1.25;letter-spacing:.2px}
  .body{font-size:9.5px;line-height:1.5;color:var(--muted);margin-top:5px}
  .copy{position:absolute;left:20px;right:20px}
  .brand{display:flex;align-items:center;gap:7px;font-family:"Montserrat",Arial,sans-serif;font-weight:700;color:var(--green-deep);font-size:15px;line-height:1.1}
  .brand__dot{width:22px;height:22px;border-radius:50%;background:var(--green);flex:none}
  .swoosh{position:absolute;left:0;top:0}
  .contact{position:absolute;left:0;right:0;text-align:center;font-family:"Montserrat",Arial,sans-serif}
  .contact__phone{font-weight:800;font-size:20px;color:var(--ink);display:flex;justify-content:center;align-items:center;gap:8px}
  .contact__addr{font-size:10px;color:var(--muted);margin-top:8px;line-height:1.5}
  .web{position:absolute;left:0;right:0;bottom:16px;text-align:center;font-family:"Montserrat",Arial,sans-serif;font-weight:600;font-size:10.5px;color:#fff}
  .cover-title{position:absolute;left:26px;right:20px;top:404px;text-align:right;font-family:"Montserrat",Arial,sans-serif;font-weight:800;font-size:17px;line-height:1.2;color:var(--green-dark);text-transform:uppercase}
  .feature{position:absolute;left:0;right:0;top:0;height:118px;background:var(--green);text-align:center;color:#fff;font-family:"Montserrat",Arial,sans-serif;padding-top:14px}
  .feature__small{font-size:12px;font-weight:600}
  .feature__big{font-size:26px;font-weight:800;line-height:1.15}
  .feature__note{font-size:9.5px;font-weight:700;letter-spacing:.4px}
  .cost{position:absolute;left:0;right:0;bottom:0;height:120px;color:#fff;text-align:center;font-family:"Montserrat",Arial,sans-serif;font-weight:800;padding-top:36px}
  .cost__label{font-size:15px}
  .cost__price{font-size:20px;line-height:1.2}
</style>
</head>
<body>

<!-- Outside spread -->
<section class="sheet sheet--outside">
  <div class="panel panel--1">
    <div class="copy" style="top:26px">
      <h2 class="heading">Personalised care in fitness and health</h2>
      <p class="body">Tailored programs designed for people of all fitness levels and ages, in a private and relaxed studio setting.</p>
      <p class="body">Our team focuses on steady progress, better movement and lasting health for every client.</p>
      <h2 class="heading" style="margin-top:14px">Experienced professionals caring for your wellbeing</h2>
      <p class="body">Each trainer brings many years of experience working with clients of all ages and health needs.</p>
    </div>
    <div class="photo" style="left:20px;top:300px;width:110px;height:120px" role="img" aria-label="Woman stretching with light dumbbells in the studio"></div>
    <div class="photo photo--warm" style="left:140px;top:300px;width:112px;height:120px" role="img" aria-label="Man training with free weights"></div>
    <div class="photo photo--food" style="left:0;top:430px;width:272px;height:125px" role="img" aria-label="Fresh vegetables and healthy food"></div>
  </div>

  <div class="panel panel--2">
    <div class="photo photo--warm" style="left:0;top:0;width:272px;height:240px" role="img" aria-label="Smiling trainer with arms crossed"></div>
    <svg class="swoosh" width="272" height="300" viewBox="0 0 272 300" aria-hidden="true">
      <path d="M0 170 C80 240 180 250 272 200 L272 300 L0 300Z" fill="var(--paper)"/>
      <path d="M0 170 C80 240 180 250 272 200 L272 214 C180 262 80 254 0 186Z" fill="var(--green)"/>
    </svg>
    <div class="brand" style="position:absolute;left:64px;top:300px"><span class="brand__dot"></span>Evergreen<br>Wellness Studio</div>
    <div class="contact" style="top:370px">
      <div class="contact__phone">
        <svg width="16" height="16" viewBox="0 0 24 24" aria-hidden="true"><path d="M6.6 10.8a15 15 0 0 0 6.6 6.6l2.2-2.2c.3-.3.7-.4 1-.2 1.1.4 2.3.6 3.6.6.6 0 1 .4 1 1V20c0 .6-.4 1-1 1A17 17 0 0 1 3 4c0-.6.4-1 1-1h3.5c.6 0 1 .4 1 1 0 1.3.2 2.5.6 3.6.1.3 0 .7-.2 1z" fill="var(--green-deep)"/></svg>
        0400 123 456
      </div>
      <div class="contact__addr">Unit 12 Level 1<br>8 Fernleaf Way Glenmore</div>
    </div>
  </div>

  <div class="panel panel--3">
    <div class="photo photo--warm" style="left:0;top:0;width:272px;height:300px" role="img" aria-label="Woman exercising with blue dumbbells"></div>
    <svg class="swoosh" width="272" height="555" viewBox="0 0 272 555" aria-hidden="true">
      <path d="M0 250 C90 330 190 300 272 250 L272 555 L0 555Z" fill="var(--paper)"/>
      <path d="M0 236 C90 316 190 286 272 236 L272 252 C190 302 90 332 0 252Z" fill="var(--green)"/>
      <path d="M0 500 C90 470 190 470 272 490 L272 555 L0 555Z" fill="var(--green)"/>
    </svg>
    <div class="brand" style="position:absolute;left:70px;top:326px"><span class="brand__dot"></span>Evergreen<br>Wellness Studio</div>
    <h1 class="cover-title">Personalised care<br>in fitness and health</h1>
    <div class="web">www.evergreenwellness.com.au</div>
  </div>
  <span class="fold" style="left:271.67px"></span><span class="fold" style="left:543.33px"></span>
</section>

<!-- Inside spread -->
<section class="sheet sheet--inside">
  <div class="panel panel--1">
    <div class="copy" style="top:22px">
      <h2 class="heading">What to expect</h2>
      <p class="body">On arrival we take time to understand your goals, history and lifestyle so every session is planned around you.</p>
      <p class="body">We work together at your pace in a calm, friendly space with no crowds and no pressure.</p>
      <h2 class="heading" style="margin-top:12px">Consultation</h2>
      <p class="body">A relaxed chat to learn about your health, habits and what you would like to achieve over time.</p>
      <h2 class="heading" style="margin-top:12px">Assessment</h2>
      <p class="body">A gentle check of strength, balance, posture and mobility gives a clear starting point for your program.</p>
    </div>
    <div class="photo photo--dark" style="left:0;top:385px;width:272px;height:170px" role="img" aria-label="Trainer guiding a client through a stretch"></div>
  </div>

  <div class="panel panel--2">
    <div class="feature">
      <div class="feature__small">Health fund claimable</div>
      <div class="feature__big">Open 7 days</div>
      <div class="feature__note">AMPLE PRIVATE PARKING AVAILABLE</div>
    </div>
    <div class="photo photo--warm" style="left:76px;top:128px;width:120px;height:120px;border-radius:50%;border:4px solid var(--green-pale)" role="img" aria-label="Client training one on one"></div>
    <div class="copy" style="top:262px">
      <h2 class="heading">The program</h2>
      <p class="body">Your program is built around your results and reviewed often so it grows with you and stays enjoyable.</p>
      <h2 class="heading" style="margin-top:12px">Nutrition</h2>
      <p class="body">Simple, practical eating advice supports your training and helps you feel better every day.</p>
    </div>
    <div class="brand" style="position:absolute;left:64px;top:470px"><span class="brand__dot"></span>Evergreen<br>Wellness Studio</div>
    <div style="position:absolute;left:0;right:0;bottom:10px;text-align:center;font-family:'Montserrat',Arial,sans-serif;font-size:9.5px;font-weight:600;color:var(--muted)">www.evergreenwellness.com.au</div>
  </div>

  <div class="panel panel--3">
    <div class="copy" style="top:22px">
      <h2 class="heading">Your sessions</h2>
      <p class="body">Sessions run one on one or in small groups, lasting about forty five minutes, with times to suit busy weeks.</p>
    </div>
    <div class="photo photo--warm" style="left:20px;top:120px;width:112px;height:95px" role="img" aria-label="Older client exercising with a band"></div>
    <div class="photo" style="left:140px;top:120px;width:112px;height:95px" role="img" aria-label="Small group exercising together"></div>
    <div class="photo" style="left:20px;top:223px;width:112px;height:95px" role="img" aria-label="Client lifting light weights"></div>
    <div class="photo photo--warm" style="left:140px;top:223px;width:112px;height:95px" role="img" aria-label="Senior couple smiling after training"></div>
    <svg class="swoosh" width="272" height="555" viewBox="0 0 272 555" aria-hidden="true">
      <path d="M0 420 C90 380 190 400 272 370 L272 555 L0 555Z" fill="var(--green)"/>
      <path d="M0 404 C90 364 190 384 272 354 L272 364 C190 394 90 374 0 414Z" fill="var(--lime)"/>
    </svg>
    <div class="cost">
      <div class="cost__label">THE COST</div>
      <div class="cost__price">$45 PAID IN BLOCKS<br>OF 5 OR 10 SESSIONS</div>
    </div>
  </div>
  <span class="fold" style="left:271.67px"></span><span class="fold" style="left:543.33px"></span>
</section>

</body>
</html>
```